Purchasing community for life science startups needs landing page for collecting of contact adresses

We are the "Vessel Alliance", the first purchasing community for life science startups. The idea is to bundle the needs of several smaller companies (laboratories) and to buy lab consumables and chemicals in larger quantities. This bargaining position, at the end of all participants can buy their products very low prices. In the attached powerpoint file you will find an idea and some elements, which demonstrate a little the style, which came into my mind.
Target Market(s)
Our target customers are startups and smaller biotech companies, which are too small to get the best prices. The aim of this landing page is to collect all interested parties.
Look and feel
Each slider illustrates characteristics of the customer's brand and the style your logo design should communicate.

```html
<!DOCTYPE html>
<html lang="en">
<head>
<meta charset="utf-8">
<title>Vessel Alliance – Shopping Community Lifescience</title>
<link rel="stylesheet" href="https://fonts.googleapis.com/css2?family=Roboto:wght@300;400;500;700;900&display=swap">
<style>
  :root{
    --blue:#1a5fb4;
    --blue-deep:#0f3f85;
    --blue-band:#1f5fbf;
    --navy:#0e2a4f;
    --ink:#222831;
    --muted:#5b6573;
    --white:#ffffff;
    --pale:#eef3f9;
    --dark:#1b1d21;
    --darker:#141518;
  }
  *{box-sizing:border-box;margin:0;padding:0}
  html,body{width:1200px;height:2620px;overflow:hidden}
  body{font-family:"Roboto",Arial,sans-serif;color:var(--ink);background:var(--white);position:relative}

  /* header */
  .site-header{position:absolute;top:0;left:0;width:1200px;height:88px;background:var(--white);display:flex;align-items:center;justify-content:space-between;padding:0 140px;box-shadow:0 2px 6px rgba(0,0,0,.08);z-index:2}
  .brand{display:flex;align-items:center;gap:12px}
  .brand-mark{width:40px;height:40px;background:var(--blue)}
  .brand-name{font-weight:700;font-size:22px;color:var(--navy);letter-spacing:1px}
  .main-nav{display:flex;align-items:center;gap:26px;font-size:15px;font-weight:500;color:var(--navy)}
  .main-nav .phone{display:flex;align-items:center;gap:8px;font-weight:700;font-size:17px}

  /* hero */
  .hero{position:absolute;top:88px;left:0;width:1200px;height:592px;overflow:hidden}
  .hero-photo{position:absolute;inset:0;background:linear-gradient(100deg,#0c2c5e 0%,#2f6fb3 35%,#7fb4de 60%,#3a72b3 80%,#163e7c 100%)}
  .hero-title{position:absolute;left:560px;top:140px;width:520px;text-align:center;color:var(--white);font-weight:700;font-size:38px;line-height:1.2;letter-spacing:1px;text-shadow:0 2px 6px rgba(0,0,0,.35)}
  .hero-curve{position:absolute;left:0;bottom:0;width:1200px;height:120px}

  /* intro */
  .intro{position:absolute;top:680px;left:0;width:1200px;height:310px;text-align:center}
  .intro h2{margin-top:30px;font-size:30px;font-weight:700;color:var(--ink)}
  .intro p{font-size:17px;line-height:1.5;color:var(--ink);margin-top:14px}
  .intro p.first{margin-top:34px}

  /* benefits */
  .benefits{position:absolute;top:990px;left:0;width:1200px;height:450px;background:linear-gradient(180deg,var(--blue-band),var(--blue-deep))}
  .benefits-media{position:absolute;left:140px;top:70px;width:340px;height:320px;background:var(--white);box-shadow:0 6px 18px rgba(0,0,0,.25);display:flex;align-items:center;justify-content:center}
  .benefits-media .box-photo{width:240px;height:220px;background:linear-gradient(150deg,#c59b68,#8f6538)}
  .benefits-copy{position:absolute;left:588px;top:110px;width:480px;color:var(--white)}
  .benefits-copy h2{font-size:32px;font-weight:500;letter-spacing:.5px}
  .benefit-list{list-style:none;margin-top:30px}
  .benefit-list li{display:flex;align-items:center;gap:12px;font-size:16px;margin-bottom:14px}
  .benefit-list svg{flex:none}
  .benefits-copy p{font-size:14px;line-height:1.55;margin-top:16px;opacity:.95}

  /* signup */
  .signup{position:absolute;top:1520px;left:0;width:1200px;height:420px;background:var(--pale)}
  .signup-photo{position:absolute;left:0;top:0;width:620px;height:420px;background:linear-gradient(120deg,#f3f6fa 0%,#cfdbe8 45%,#7ea3c8 75%,#e8eef5 100%)}
  .signup-form{position:absolute;left:780px;top:110px;width:290px}
  .signup-form .field{display:block;height:36px;border:1px solid #c9d2dc;background:var(--white);font-size:12px;color:var(--muted);padding:0 12px;line-height:34px;margin-bottom:18px}
  .signup-form .submit{display:block;height:40px;background:var(--blue);color:var(--white);text-align:center;line-height:40px;font-weight:700;font-size:14px;letter-spacing:1px}

  /* principles */
  .principles{position:absolute;top:1960px;left:0;width:1200px;height:440px;background:var(--dark)}
  .card{position:absolute;top:80px;width:280px;height:320px;background:var(--white);text-align:center;padding:72px 26px 0}
  .card .icon{position:absolute;top:-36px;left:104px;width:72px;height:72px;border-radius:50%;background:var(--blue);border:4px solid var(--white);display:flex;align-items:center;justify-content:center}
  .card h3{font-size:19px;font-weight:700;color:var(--ink);letter-spacing:.5px}
  .card p{font-size:13px;line-height:1.6;color:var(--muted);margin-top:18px}
  .card-goal{left:140px}
  .card-principle{left:460px}
  .card-simple{left:780px}

  /* footer */
  .site-footer{position:absolute;top:2400px;left:0;width:1200px;height:220px;background:var(--darker);color:#d7dbe0;text-align:center;font-size:14px}
  .site-footer .company{margin-top:26px;font-weight:700;font-size:16px;color:var(--white)}
  .site-footer .links{margin-top:16px}
  .site-footer .copy{margin-top:16px}
  .social{display:flex;justify-content:center;gap:12px;margin-top:22px}
  .social span{width:30px;height:30px;border-radius:50%;border:2px solid #d7dbe0}
</style>
</head>
<body>

<header class="site-header">
  <div class="brand">
    <span class="brand-mark"></span>
    <span class="brand-name">VESSEL ALLIANCE</span>
  </div>
  <nav class="main-nav">
    <span>HOME</span><span>ABOUT US</span><span>HOW IT WORKS</span><span>CONTACT</span>
    <span class="phone">
      <svg width="18" height="18" viewBox="0 0 24 24"><path fill="#0e2a4f" d="M6.6 10.8a15 15 0 0 0 6.6 6.6l2.2-2.2c.3-.3.7-.4 1-.2 1.1.4 2.3.6 3.6.6.6 0 1 .4 1 1V20c0 .6-.4 1-1 1A17 17 0 0 1 3 4c0-.6.4-1 1-1h3.5c.6 0 1 .4 1 1 0 1.3.2 2.5.6 3.6.1.3 0 .7-.2 1z"/></svg>
      0800 123 456
    </span>
  </nav>
</header>

<section class="hero">
  <div class="hero-photo" role="img" aria-label="Laboratory scene with a researcher's gloved hand holding a test tube and coloured glassware on a bench"></div>
  <h1 class="hero-title">SHOPPING COMMUNITY<br>LIFESCIENCE</h1>
  <svg class="hero-curve" viewBox="0 0 1200 120" preserveAspectRatio="none">
    <path d="M0 70 Q600 -10 1200 70 L1200 120 L0 120 Z" fill="#1a5fb4"/>
    <path d="M0 84 Q600 8 1200 84 L1200 120 L0 120 Z" fill="#ffffff"/>
  </svg>
</section>

<section class="intro">
  <h2>JOINT PURCHASE AT WHOLESALE PRICES</h2>
  <p class="first">Do you run a LifeScience lab?<br>Do you need chemicals, laboratory glassware and consumables regularly?</p>
  <p>Are your purchase quantities too small to receive maximum discounts?</p>
  <p>Then take part in the first lab campaign 2019 and Save up to 40% on purchases.</p>
</section>

<section class="benefits">
  <div class="benefits-media">
    <div class="box-photo" role="img" aria-label="Cardboard shipping box of lab supplies"></div>
  </div>
  <div class="benefits-copy">
    <h2>BENEFITS FOR PARTICIPANTS</h2>
    <ul class="benefit-list">
      <li><svg width="18" height="18" viewBox="0 0 18 18"><circle cx="9" cy="9" r="8" fill="none" stroke="#fff" stroke-width="1.5"/><path d="M5 9.3l2.6 2.5L13 6.5" fill="none" stroke="#fff" stroke-width="1.8"/></svg>Buy at wholesale prices</li>
      <li><svg width="18" height="18" viewBox="0 0 18 18"><circle cx="9" cy="9" r="8" fill="none" stroke="#fff" stroke-width="1.5"/><path d="M5 9.3l2.6 2.5L13 6.5" fill="none" stroke="#fff" stroke-width="1.8"/></svg>No negotiations with suppliers</li>
      <li><svg width="18" height="18" viewBox="0 0 18 18"><circle cx="9" cy="9" r="8" fill="none" stroke="#fff" stroke-width="1.5"/><path d="M5 9.3l2.6 2.5L13 6.5" fill="none" stroke="#fff" stroke-width="1.8"/></svg>No contract obligation</li>
    </ul>
    <p>Are you interested in participating? Then please do not hesitate to sign up for our list of interested parties.</p>
    <p>To get an impression of our prices, we send you a preliminary price list and ask for feedback. Which articles interest you? In what quantities do you need them? Which are still missing?</p>
  </div>
</section>

<section class="signup">
  <div class="signup-photo" role="img" aria-label="Researchers in lab coats and safety glasses working at a laboratory bench"></div>
  <form class="signup-form">
    <span class="field">Email Address</span>
    <span class="field">Last Name</span>
    <span class="field">First Name</span>
    <span class="submit">SUBMIT</span>
  </form>
</section>

<section class="principles">
  <article class="card card-goal">
    <div class="icon"><svg width="34" height="34" viewBox="0 0 34 34"><circle cx="17" cy="17" r="14" fill="none" stroke="#fff" stroke-width="2.5"/><circle cx="17" cy="17" r="8" fill="none" stroke="#fff" stroke-width="2.5"/><circle cx="17" cy="17" r="3" fill="#fff"/></svg></div>
    <h3>OUR GOAL</h3>
    <p>Our aim is to build the first life science purchasing community that lets every participant cover their lab supplies at wholesale prices.</p>
  </article>
  <article class="card card-principle">
    <div class="icon"><svg width="34" height="34" viewBox="0 0 34 34"><path d="M13 4h8M15 4v10L7 28c-.8 1.4.2 3 1.8 3h16.4c1.6 0 2.6-1.6 1.8-3L19 14V4" fill="none" stroke="#fff" stroke-width="2.5" stroke-linejoin="round"/><path d="M10 23h14" stroke="#fff" stroke-width="2.5"/></svg></div>
    <h3>THE CAMPAIGN PRINCIPLE</h3>
    <p>We bundle your yearly demand for chemicals, consumables and lab supplies and act as a strong partner toward suppliers. More participants mean more bargaining power and better prices.</p>
  </article>
  <article class="card card-simple">
    <div class="icon"><svg width="34" height="34" viewBox="0 0 34 34"><path d="M4 5h13l13 13-12 12L5 17z" fill="none" stroke="#fff" stroke-width="2.5" stroke-linejoin="round"/><circle cx="11" cy="11" r="2.5" fill="#fff"/></svg></div>
    <h3>KEEP IT SIMPLE</h3>
    <p>No framework contracts, minimum quantities or other obligations. If you like the negotiated price, simply order what your lab needs through the campaign.</p>
  </article>
</section>

<footer class="site-footer">
  <p class="company">Vessel Alliance Purchasing E.K.</p>
  <p class="links">Imprint &nbsp;|&nbsp; Data Protection</p>
  <p class="copy">Copyright © 2019 Vessel Alliance. All Rights Reserved</p>
  <div class="social"><span></span><span></span><span></span></div>
</footer>

</body>
</html>
```